A3 Poster & DL Flyer Design Project

We need a poster and flyer designed to advertise a Wine, Food and Live music event.
Event title is "An Evening Under Vines" and is put on by Holloway's Ridge Wines. Date for the event is Sunday 21 April 2013
The outdoor event covers wine, gourmet food and live music
Live music genera is Jazz, Blues, Swing

Reason: Most of the designs did not meet our requirements only 3 out of 21 have potential but would like to see more

Target Market(s)

25 - 55 wine drinkers with money.

Industry/Entity Type

Event

Requirements
Must have
• Title of the Event "An Evening Under Vinez"
Date Sunday 21 April 2013 or be generic where we can write the date on each year.
Camel Logo
Entry is Free
No BYO Alcohol
Must reflect Wine, Food & Live Music

```html
<!DOCTYPE html>
<html lang="en">
<head>
<meta charset="utf-8">
<title>An Evening Under Vines</title>
<link rel="stylesheet" href="https://fonts.googleapis.com/css2?family=Bebas+Neue&family=Lobster&display=swap">
<style>
  :root {
    --poster-yellow: #f2ff00;
    --ink: #1e1e1e;
    --wine-light: #8a2a12;
    --wine-dark: #3a0c0c;
    --fork-grey: #8a8a8a;
  }
  html, body {
    margin: 0;
    padding: 0;
    overflow: hidden;
    background: var(--poster-yellow);
  }
  .poster {
    position: relative;
    width: 848px;
    height: 1200px;
    background: var(--poster-yellow);
    color: var(--ink);
    font-family: "Bebas Neue", "Arial Narrow", sans-serif;
    overflow: hidden;
  }
  .event-title {
    position: absolute;
    left: 182px;
    top: 118px;
    margin: 0;
    font-size: 108px;
    font-weight: 400;
    line-height: 114px;
    letter-spacing: 0;
    text-transform: uppercase;
    white-space: nowrap;
  }
  .event-title span { display: block; }
  .host {
    position: absolute;
    left: 182px;
    top: 590px;
    margin: 0;
    font-family: "Lobster", cursive;
    font-size: 21px;
    white-space: nowrap;
  }
  .event-date {
    position: absolute;
    left: 182px;
    top: 690px;
    margin: 0;
    text-transform: uppercase;
  }
  .event-date .day {
    display: block;
    font-size: 60px;
    line-height: 64px;
  }
  .event-date .month {
    display: block;
    font-size: 42px;
    line-height: 46px;
  }
  .highlights {
    position: absolute;
    left: 182px;
    top: 876px;
    margin: 0;
    padding: 0;
    list-style: none;
    font-size: 40px;
    line-height: 43px;
    text-transform: uppercase;
  }
  .entry-notes {
    position: absolute;
    left: 182px;
    top: 1088px;
    margin: 0;
    font-size: 26px;
    line-height: 30px;
    text-transform: uppercase;
    white-space: nowrap;
  }
  .winery-mark {
    position: absolute;
    left: 498px;
    top: 1088px;
    display: flex;
    align-items: center;
    gap: 10px;
    font-size: 26px;
    line-height: 30px;
    text-transform: uppercase;
    white-space: nowrap;
  }
  .winery-mark .dot {
    width: 18px;
    height: 18px;
    border-radius: 50%;
    background: var(--ink);
  }
  .artwork {
    position: absolute;
    left: 498px;
    top: 114px;
  }
</style>
</head>
<body>
  <main class="poster">
    <h1 class="event-title">
      <span>An</span>
      <span>Evening</span>
      <span>Under</span>
      <span>Vines</span>
    </h1>
    <p class="host">by Holloway's Ridge Wines</p>

    <p class="event-date">
      <span class="day">Sunday 21</span>
      <span class="month">April 2013</span>
    </p>

    <ul class="highlights">
      <li>Wine</li>
      <li>Gourmet Food</li>
      <li>And</li>
      <li>Live Music</li>
    </ul>

    <p class="entry-notes">Free Entry · No BYO Alcohol</p>

    <div class="winery-mark">
      <span class="dot"></span>
      <span>Holloway's Ridge Wines</span>
    </div>

    <svg class="artwork" width="156" height="926" viewBox="0 0 156 926" role="img"
         aria-label="Illustration of a guitar headstock joined to a red wine bottle that ends in a fork">
      <defs>
        <linearGradient id="artwork-tones" x1="0" y1="0" x2="0" y2="1">
          <stop offset="0" stop-color="var(--wine-light)"/>
          <stop offset="0.45" stop-color="var(--wine-dark)"/>
          <stop offset="0.7" stop-color="var(--wine-dark)"/>
          <stop offset="0.72" stop-color="var(--fork-grey)"/>
          <stop offset="1" stop-color="var(--fork-grey)"/>
        </linearGradient>
      </defs>
      <rect x="0" y="0" width="156" height="926" fill="url(#artwork-tones)"/>
    </svg>
  </main>
</body>
</html>
```